Illustration Design Project

We need two simple, clean circle illustrations of the Hero's Journey that use our terminology. These will be used for Power Point presentations and other paper support docs as part of our programs that help writers, authors, and thought leaders create and shape their books.

We would like to see designs that
- have a white or off-white background complemented with our branded orange and red
- divided according to the attached illustration into 3 Acts
- move clock wise (not counter-clock wise)

The final design should communicate adventure and courage.

Designers should visit pebble lantern.com to understand the company branding colors and logos.

Target Market(s)

writers, authors, thought leaders, coaches, business people who are writing books

Industry/Entity Type

It Company

Requirements
Must have
• - have a white or off-white background complemented with our branded orange and red
- be super-clean and easy-to-read
Nice to have
• nothing too fancy - but if you have an idea to evoke courage without it being corny, that would be fine
Should not have
• Do not go for cliched "journey"-like images.

```html
<!DOCTYPE html>
<html lang="en">
<head>
<meta charset="utf-8">
<title>The Hero's Journey</title>
<link href="https://fonts.googleapis.com/css2?family=Carlito:wght@400;700&display=swap" rel="stylesheet">
<style>
  :root {
    --bg-offwhite: #fdfaf4;
    --ink-dark: #2b2522;
    --brand-red: #e3211b;
    --brand-red-soft: #f6c9c4;
    --brand-orange: #ff8a1f;
    --brand-orange-deep: #f26a0f;
    --act1-gold: #ffc21a;
    --act1-label: #e09a00;
    --badge-blue-light: #6fa8ff;
    --badge-blue-dark: #1c3fae;
    --badge-gold-light: #fff2a0;
    --badge-gold-dark: #d9a400;
    --badge-ink-dark: #3a2a00;
  }
  html, body {
    margin: 0;
    padding: 0;
    width: 1200px;
    height: 900px;
    overflow: hidden;
    background: var(--bg-offwhite);
  }
  .journey-canvas {
    display: block;
    width: 1200px;
    height: 900px;
    font-family: "Carlito", "Calibri", sans-serif;
  }
  .stage-label {
    fill: var(--ink-dark);
    font-size: 25px;
  }
  .act-label {
    font-size: 28px;
    font-weight: 700;
  }
  .act-label--one { fill: var(--act1-label); }
  .act-label--two { fill: var(--brand-red); }
  .act-label--three { fill: var(--brand-orange-deep); }
  .world-label {
    font-size: 27px;
    font-weight: 700;
  }
  .world-label--ordinary { fill: var(--brand-orange-deep); }
  .world-label--new { fill: var(--brand-red); }
  .badge-ring { stroke: #ffffff; stroke-width: 2.5; }
  .badge-number {
    font-size: 22px;
    font-weight: 700;
    text-anchor: middle;
    dominant-baseline: central;
  }
  .badge-number--blue { fill: #ffffff; }
  .badge-number--gold { fill: var(--badge-ink-dark); }
</style>
</head>
<body>
<svg class="journey-canvas" viewBox="0 0 1200 900" xmlns="http://www.w3.org/2000/svg" role="img" aria-label="Hero's Journey cycle in three acts">
  <defs>
    <radialGradient id="badgeBlue" cx="35%" cy="30%" r="75%">
      <stop offset="0" stop-color="var(--badge-blue-light)"/>
      <stop offset="1" stop-color="var(--badge-blue-dark)"/>
    </radialGradient>
    <radialGradient id="badgeGold" cx="35%" cy="30%" r="75%">
      <stop offset="0" stop-color="var(--badge-gold-light)"/>
      <stop offset="1" stop-color="var(--badge-gold-dark)"/>
    </radialGradient>
    <linearGradient id="actThreeFill" x1="0" y1="1" x2="0.6" y2="0">
      <stop offset="0" stop-color="var(--brand-orange-deep)"/>
      <stop offset="1" stop-color="var(--brand-orange)"/>
    </linearGradient>
    <linearGradient id="dividerFill" x1="0" y1="0" x2="1" y2="0">
      <stop offset="0" stop-color="var(--brand-red-soft)" stop-opacity="0"/>
      <stop offset="0.2" stop-color="var(--brand-red-soft)" stop-opacity="1"/>
      <stop offset="0.8" stop-color="var(--brand-red-soft)" stop-opacity="1"/>
      <stop offset="1" stop-color="var(--brand-red-soft)" stop-opacity="0"/>
    </linearGradient>
  </defs>

  <g class="world-divider">
    <rect x="60" y="458" width="1000" height="16" fill="url(#dividerFill)"/>
    <rect x="350" y="465" width="400" height="2" fill="var(--brand-red)" opacity="0.8"/>
  </g>
  <text class="world-label world-label--ordinary" x="550" y="451" text-anchor="middle">The Ordinary World</text>
  <text class="world-label world-label--new" x="550" y="503" text-anchor="middle">The New World</text>

  <g class="act-arc act-arc--one">
    <path d="M548 135 A308 308 0 0 1 853 400" fill="none" stroke="var(--act1-gold)" stroke-width="30"/>
    <polygon points="818,396 892,392 858,440" fill="var(--act1-gold)"/>
  </g>

  <g class="act-arc act-arc--two">
    <path d="M856 450 A308 308 0 0 1 256 540" fill="none" stroke="var(--brand-red)" stroke-width="30"/>
    <rect x="840" y="448" width="32" height="8" fill="var(--brand-red)"/>
    <polygon points="218,546 294,540 246,490" fill="var(--brand-red)"/>
  </g>

  <g class="act-arc act-arc--three">
    <path d="M240 445 A308 308 0 0 1 458 148" fill="none" stroke="url(#actThreeFill)" stroke-width="30"/>
    <polygon points="446,112 468,184 522,138" fill="var(--brand-orange)"/>
  </g>

  <text class="act-label act-label--one" transform="translate(690 214) rotate(55)">ACT 1</text>
  <text class="act-label act-label--two" x="546" y="690" text-anchor="middle">ACT 2</text>
  <text class="act-label act-label--three" transform="translate(340 302) rotate(-60)">ACT 3</text>

  <g class="stage-badges">
    <circle class="badge-ring" cx="548" cy="123" r="21" fill="url(#badgeBlue)"/><text class="badge-number badge-number--blue" x="548" y="124">1</text>
    <circle class="badge-ring" cx="688" cy="150" r="21" fill="url(#badgeBlue)"/><text class="badge-number badge-number--blue" x="688" y="151">2</text>
    <circle class="badge-ring" cx="790" cy="232" r="21" fill="url(#badgeBlue)"/><text class="badge-number badge-number--blue" x="790" y="233">3</text>
    <circle class="badge-ring" cx="850" cy="342" r="21" fill="url(#badgeBlue)"/><text class="badge-number badge-number--blue" x="850" y="343">4</text>
    <circle class="badge-ring" cx="858" cy="490" r="21" fill="url(#badgeGold)"/><text class="badge-number badge-number--gold" x="858" y="491">5</text>
    <circle class="badge-ring" cx="810" cy="606" r="21" fill="url(#badgeGold)"/><text class="badge-number badge-number--gold" x="810" y="607">6</text>
    <circle class="badge-ring" cx="727" cy="690" r="21" fill="url(#badgeGold)"/><text class="badge-number badge-number--gold" x="727" y="691">7</text>
    <circle class="badge-ring" cx="548" cy="745" r="21" fill="url(#badgeGold)"/><text class="badge-number badge-number--gold" x="548" y="746">8</text>
    <circle class="badge-ring" cx="320" cy="640" r="21" fill="url(#badgeGold)"/><text class="badge-number badge-number--gold" x="320" y="641">9</text>
    <circle class="badge-ring" cx="240" cy="445" r="21" fill="url(#badgeBlue)"/><text class="badge-number badge-number--blue" x="240" y="446">10</text>
    <circle class="badge-ring" cx="273" cy="290" r="21" fill="url(#badgeBlue)"/><text class="badge-number badge-number--blue" x="273" y="291">11</text>
    <circle class="badge-ring" cx="380" cy="172" r="21" fill="url(#badgeBlue)"/><text class="badge-number badge-number--blue" x="380" y="173">12</text>
  </g>

  <g class="stage-labels">
    <text class="stage-label" x="653" y="86" text-anchor="middle">The Ordinary World</text>
    <text class="stage-label" x="742" y="150">The Call to Adventure</text>
    <text class="stage-label" x="832" y="241">Refusal of the Call</text>
    <text class="stage-label" x="897" y="346">Meeting</text>
    <text class="stage-label" x="897" y="382">with Mentor</text>
    <text class="stage-label" x="897" y="493">Crossing the First</text>
    <text class="stage-label" x="897" y="529">Threshold</text>
    <text class="stage-label" x="852" y="612">Test, Allies,</text>
    <text class="stage-label" x="852" y="646">Enemies</text>
    <text class="stage-label" x="720" y="740">Approach to</text>
    <text class="stage-label" x="720" y="776">the Inmost Cave</text>
    <text class="stage-label" x="548" y="803" text-anchor="middle">Supreme Ordeal</text>
    <text class="stage-label" x="205" y="672" text-anchor="middle">Reward</text>
    <text class="stage-label" x="205" y="706" text-anchor="middle">(Seizing the Sword)</text>
    <text class="stage-label" x="207" y="410" text-anchor="end">The Road</text>
    <text class="stage-label" x="207" y="446" text-anchor="end">Back</text>
    <text class="stage-label" x="237" y="300" text-anchor="end">Resurrection</text>
    <text class="stage-label" x="338" y="164" text-anchor="end">Return with</text>
    <text class="stage-label" x="338" y="199" text-anchor="end">the Elixir</text>
  </g>
</svg>
</body>
</html>
```